Loose Saltbush Venture

I am creating a personal blog to outline, in pictures and words, the cultural decay of everyday life in Australia today. This has been manifested by the rise of a nanny state.
Australia's foundation was based on hardened men i.e.- convicts, lifeguards, determined, strong men. Today Australia has become a Nanny State where everything is banned e.g.- it's illegal not to wear a helmet on a bike; it's illegal to chop down or prune trees on your own property. It's now a place where a city parking space might have 7-10 signs outlining a different set of parking laws for different timezones and days of the week. I could type forever.
Obviously I am looking for a neat wordpress designed blog with a focus on having a great banner that gives an indication of this change. From strong, determined individuals to a nation being forced to cower under a nanny. I'm open to your interpretation.
The blog title is "Loose Saltbush" with a byline of "what the bloody hell happened".

```html
<!DOCTYPE html>
<html lang="en">
<head>
<meta charset="utf-8">
<title>Loose Saltbush</title>
<link href="https://fonts.googleapis.com/css2?family=Roboto:ital,wght@0,400;0,500;0,700;1,400&display=swap" rel="stylesheet">
<style>
:root{
  --accent:#d04651;
  --ink:#222;
  --body:#666;
  --muted:#888;
  --line:#e3e3e3;
  --page:#f4f4f4;
  --white:#fff;
  --footer:#1c1c1c;
  --star:#f2b01e;
  --star-off:#ccc;
}
*{box-sizing:border-box;margin:0;padding:0}
html,body{width:1200px;height:2975px;overflow:hidden}
body{position:relative;background:var(--page);font-family:"Roboto",Arial,sans-serif;color:var(--ink)}
.abs{position:absolute}

/* header */
.site-header{left:0;top:0;width:1200px;height:91px;background:var(--white)}
.brand{left:97px;top:24px;font-size:38px;font-weight:700;color:var(--ink);letter-spacing:-.5px}
.main-nav{left:480px;top:34px;display:flex;gap:0;font-size:16px;color:#333}
.main-nav span{margin-right:32px}
.search-icon{left:1080px;top:35px}

/* hero */
.hero{left:0;top:91px;width:1200px;height:480px;background:linear-gradient(180deg,#c99a78 0%,#7d8aa0 28%,#3f6f8f 55%,#2f5a4a 82%,#2b4a2f 100%)}
.hero-caption{left:702px;top:248px;width:379px;height:174px;background:rgba(20,20,20,.72);padding:22px 28px}
.hero-title{font-size:36px;font-weight:700;color:var(--white);line-height:41px;text-transform:uppercase}
.hero-btn{display:inline-block;margin-top:14px;border:2px solid var(--white);color:var(--white);font-size:13px;padding:7px 14px;border-radius:3px}
.hero-arrow{top:313px;width:34px;height:36px;background:rgba(0,0,0,.55);display:flex;align-items:center;justify-content:center}

/* feature tiles */
.tile{top:623px;width:324px;height:236px}
.tile .label{position:absolute;left:22px;top:152px;background:var(--accent);color:var(--white);font-size:10px;font-weight:700;padding:3px 7px}
.tile .caption{position:absolute;left:22px;top:180px;color:var(--white);font-size:14px;line-height:19px}
.tile .shade{position:absolute;left:0;bottom:0;width:100%;height:110px;background:linear-gradient(180deg,rgba(0,0,0,0),rgba(0,0,0,.7))}

/* posts */
.post{left:99px;width:698px;height:284px;background:var(--white);border:1px solid var(--line);display:flex}
.post-thumb{width:307px;height:282px;flex:none}
.post-body{padding:26px 28px 0 28px}
.post-title{font-size:18px;line-height:23px;color:var(--ink);font-weight:400}
.post-meta{display:flex;gap:34px;margin-top:20px;font-size:12px;font-style:italic;color:var(--muted);align-items:center}
.post-meta span{display:flex;align-items:center;gap:8px}
.post-excerpt{margin-top:16px;font-size:11.5px;line-height:20.5px;color:var(--body)}
.read-more{display:inline-block;margin-top:12px;background:var(--accent);color:var(--white);font-size:11px;width:101px;height:30px;line-height:30px;text-align:center}

/* sidebar */
.widget{left:839px;width:262px;background:var(--white);border:1px solid var(--line)}
.widget-head{height:42px;background:var(--accent);color:var(--white);font-size:18px;font-weight:500;padding:11px 12px;text-transform:uppercase}
.member{display:flex;align-items:flex-start;gap:16px;padding:0 16px;height:112px;padding-top:18px}
.avatar{width:88px;height:88px;border-radius:50%;flex:none}
.member-name{font-size:13px;color:#333;margin-top:8px}
.member-role{font-size:13px;color:var(--body);margin-top:4px}
.stars{display:flex;gap:2px;margin-top:6px}
.recent{display:flex;gap:12px;padding:0 16px;height:163px;padding-top:34px}
.recent-thumb{width:101px;height:111px;flex:none}
.recent-title{font-size:13px;color:#333;margin-top:2px}
.recent-text{font-size:11px;line-height:18px;color:var(--body);margin-top:8px}
.recent-meta{font-size:10px;font-style:italic;color:var(--muted);margin-top:8px;display:flex;gap:6px;align-items:center}
.archive-list{list-style:none;padding:14px 18px 0;font-size:12px;color:#444}
.archive-list li{height:28.5px}
.video-thumb{left:839px;top:2213px;width:262px;height:171px;background:linear-gradient(180deg,#8fb0d6 0%,#b9a58c 55%,#5c7a3c 100%)}
.video-play{left:944px;top:2272px}
.video-text{left:839px;top:2400px;width:262px;font-size:11.5px;line-height:19px;color:var(--body)}

/* pagination */
.pagination{left:99px;top:2521px;display:flex;gap:8px}
.pagination span{height:24px;min-width:24px;padding:0 6px;border:1px solid #ccc;background:var(--white);font-size:11px;line-height:22px;text-align:center;color:#333}
.pagination .wide{min-width:48px}

/* footer */
.site-footer{left:0;top:2612px;width:1200px;height:363px;background:var(--footer);color:var(--white)}
.foot-head{top:2652px;font-size:19px;font-weight:500;text-transform:uppercase;color:var(--white)}
.foot-text{font-size:11.5px;line-height:20px;color:#ddd}
.email-field{left:99px;top:2749px;width:285px;height:41px;background:var(--white);color:#999;font-size:11px;padding:13px 14px}
.subscribe-btn{left:99px;top:2800px;width:98px;height:42px;background:var(--accent);color:var(--white);font-size:12px;line-height:42px;text-align:center}
.contact-row{display:flex;gap:14px;font-size:12px;line-height:20px;color:#ddd;margin-bottom:12px}
.quick-links{list-style:none;font-size:12px;line-height:23.5px;color:#ddd}
.social{width:78px;height:78px;display:flex;flex-direction:column;align-items:center;justify-content:flex-end;padding-bottom:10px;font-size:12px;line-height:15px;color:var(--white);text-align:center}
.social.fb{background:#3b5b98}.social.tw{background:#1da1e2}.social.in{background:#1a7fb5}.social.yt{background:#d2262a}
.copyright{left:0;top:2933px;width:1200px;text-align:center;font-size:12px;color:#ccc}
.foot-rule{left:0;top:2912px;width:1200px;height:1px;background:#2c2c2c}
</style>
</head>
<body>

<header class="site-header abs">
  <div class="brand abs">Loose Saltbush</div>
  <nav class="main-nav abs">
    <span>Home</span><span>Cultural</span><span>About Us</span><span>Videos</span><span>Subscriptions</span><span>Contacts</span>
  </nav>
  <svg class="search-icon abs" width="18" height="18" viewBox="0 0 18 18"><circle cx="7.5" cy="7.5" r="5.5" fill="none" stroke="#222" stroke-width="2.4"/><line x1="11.5" y1="11.5" x2="16.5" y2="16.5" stroke="#222" stroke-width="2.6" stroke-linecap="round"/></svg>
</header>

<section class="hero abs" role="img" aria-label="Harbour city at dusk with a steel arch bridge and boats moored on the water"></section>
<div class="hero-caption abs">
  <h1 class="hero-title">What the bloody<br>hell happened</h1>
  <span class="hero-btn">READ MORE</span>
</div>
<div class="hero-arrow abs" style="left:62px"><svg width="12" height="16" viewBox="0 0 12 16"><path d="M9 2 3 8l6 6" fill="none" stroke="#fff" stroke-width="2.5"/></svg></div>
<div class="hero-arrow abs" style="left:1100px"><svg width="12" height="16" viewBox="0 0 12 16"><path d="M3 2l6 6-6 6" fill="none" stroke="#fff" stroke-width="2.5"/></svg></div>

<article class="tile abs" style="left:99px;background:linear-gradient(160deg,#c9a46a,#6d5a3e 60%,#3a2f22)" role="img" aria-label="Two riders in helmets on a motorbike">
  <div class="shade"></div><span class="label">NEWS</span>
  <p class="caption">Wear a helmet on a bike<br>simply dummy Text of the printing</p>
</article>
<article class="tile abs" style="left:436px;background:linear-gradient(160deg,#4f8bc4,#6b8d4a 55%,#3c4a2a)" role="img" aria-label="Arborist in safety gear pruning a tall tree">
  <div class="shade"></div><span class="label">VIDEOS</span>
  <p class="caption">Prune trees on your own property<br>Text of the printing</p>
</article>
<article class="tile abs" style="left:775px;background:linear-gradient(160deg,#8aa4c0,#7a6a5a 55%,#3a3430)" role="img" aria-label="City street lined with parked cars and old buildings">
  <div class="shade"></div><span class="label">NEWS</span>
  <p class="caption">A city parking space<br>Ipsum is simply dummy of the printing</p>
</article>

<!-- post list -->
<article class="post abs" style="top:912px">
  <div class="post-thumb" style="background:linear-gradient(150deg,#6f9a4a,#a89a7a 55%,#4f5a3a)" role="img" aria-label="Traveller feeding a kangaroo in a wildlife park"></div>
  <div class="post-body">
    <h2 class="post-title">Nemo enim ipsam voluptatem quia<br>voluptas sit aspernatur</h2>
    <div class="post-meta">
      <span><svg width="11" height="11" viewBox="0 0 11 11"><rect x="1" y="2" width="9" height="8" fill="none" stroke="#888"/><line x1="1" y1="4.5" x2="10" y2="4.5" stroke="#888"/></svg>Jan 25, 2017</span>
      <span><svg width="12" height="11" viewBox="0 0 12 11"><path d="M1 1h10v7H5l-3 2V8H1z" fill="none" stroke="#888"/></svg>2 comments</span>
      <span><svg width="11" height="11" viewBox="0 0 11 11"><path d="M2 9 9 2" stroke="#888" stroke-width="2"/></svg>by Dale</span>
    </div>
    <p class="post-excerpt">Sed ut perspiciatis unde omnis iste natus error sit voluptatem<br>accusantium doloremque laudantium, totam rem aperiam, eaque<br>ipsa quae ab illo inventore veritatis et quasi architecto beatae<br>vitae dicta sunt explicabo. Nemo enim ipsam</p>
    <span class="read-more">READ MORE &gt;&gt;</span>
  </div>
</article>
<article class="post abs" style="top:1225px">
  <div class="post-thumb" style="background:linear-gradient(180deg,#4c86c8,#9fb6cf 35%,#3f6a3a 70%,#2e4a26)" role="img" aria-label="Cable car over a forested valley with sandstone cliffs"></div>
  <div class="post-body">
    <h2 class="post-title">Nemo enim ipsam voluptatem quia<br>voluptas sit aspernatur</h2>
    <div class="post-meta">
      <span><svg width="11" height="11" viewBox="0 0 11 11"><rect x="1" y="2" width="9" height="8" fill="none" stroke="#888"/><line x1="1" y1="4.5" x2="10" y2="4.5" stroke="#888"/></svg>Jan 25, 2017</span>
      <span><svg width="12" height="11" viewBox="0 0 12 11"><path d="M1 1h10v7H5l-3 2V8H1z" fill="none" stroke="#888"/></svg>2 comments</span>
      <span><svg width="11" height="11" viewBox="0 0 11 11"><path d="M2 9 9 2" stroke="#888" stroke-width="2"/></svg>by Dale</span>
    </div>
    <p class="post-excerpt">Sed ut perspiciatis unde omnis iste natus error sit voluptatem<br>accusantium doloremque laudantium, totam rem aperiam, eaque<br>ipsa quae ab illo inventore veritatis et quasi architecto beatae<br>vitae dicta sunt explicabo. Nemo enim ipsam</p>
    <span class="read-more">READ MORE &gt;&gt;</span>
  </div>
</article>
<article class="post abs" style="top:1541px">
  <div class="post-thumb" style="background:linear-gradient(150deg,#5a5a4a,#8a6a4a 50%,#2e2a22)" role="img" aria-label="Performer with painted body at a smoking ceremony"></div>
  <div class="post-body">
    <h2 class="post-title">Nemo enim ipsam voluptatem quia<br>voluptas sit aspernatur</h2>
    <div class="post-meta">
      <span><svg width="11" height="11" viewBox="0 0 11 11"><rect x="1" y="2" width="9" height="8" fill="none" stroke="#888"/><line x1="1" y1="4.5" x2="10" y2="4.5" stroke="#888"/></svg>Jan 25, 2017</span>
      <span><svg width="12" height="11" viewBox="0 0 12 11"><path d="M1 1h10v7H5l-3 2V8H1z" fill="none" stroke="#888"/></svg>2 comments</span>
      <span><svg width="11" height="11" viewBox="0 0 11 11"><path d="M2 9 9 2" stroke="#888" stroke-width="2"/></svg>by Dale</span>
    </div>
    <p class="post-excerpt">Sed ut perspiciatis unde omnis iste natus error sit voluptatem<br>accusantium doloremque laudantium, totam rem aperiam, eaque<br>ipsa quae ab illo inventore veritatis et quasi architecto beatae<br>vitae dicta sunt explicabo. Nemo enim ipsam</p>
    <span class="read-more">READ MORE &gt;&gt;</span>
  </div>
</article>
<article class="post abs" style="top:1857px">
  <div class="post-thumb" style="background:linear-gradient(150deg,#a0b8c8,#b88a5a 45%,#6a3a2a)" role="img" aria-label="Large painted mural on the side of an old building"></div>
  <div class="post-body">
    <h2 class="post-title">Nemo enim ipsam voluptatem quia<br>voluptas sit aspernatur</h2>
    <div class="post-meta">
      <span><svg width="11" height="11" viewBox="0 0 11 11"><rect x="1" y="2" width="9" height="8" fill="none" stroke="#888"/><line x1="1" y1="4.5" x2="10" y2="4.5" stroke="#888"/></svg>Jan 25, 2017</span>
      <span><svg width="12" height="11" viewBox="0 0 12 11"><path d="M1 1h10v7H5l-3 2V8H1z" fill="none" stroke="#888"/></svg>2 comments</span>
      <span><svg width="11" height="11" viewBox="0 0 11 11"><path d="M2 9 9 2" stroke="#888" stroke-width="2"/></svg>by Dale</span>
    </div>
    <p class="post-excerpt">Sed ut perspiciatis unde omnis iste natus error sit voluptatem<br>accusantium doloremque laudantium, totam rem aperiam, eaque<br>ipsa quae ab illo inventore veritatis et quasi architecto beatae<br>vitae dicta sunt explicabo. Nemo enim ipsam</p>
    <span class="read-more">READ MORE &gt;&gt;</span>
  </div>
</article>
<article class="post abs" style="top:2173px">
  <div class="post-thumb" style="background:linear-gradient(150deg,#3a4a6a,#b07a6a 50%,#4a2e3a)" role="img" aria-label="Shopper browsing colourful goods at a market stall"></div>
  <div class="post-body">
    <h2 class="post-title">Nemo enim ipsam voluptatem quia<br>voluptas sit aspernatur</h2>
    <div class="post-meta">
      <span><svg width="11" height="11" viewBox="0 0 11 11"><rect x="1" y="2" width="9" height="8" fill="none" stroke="#888"/><line x1="1" y1="4.5" x2="10" y2="4.5" stroke="#888"/></svg>Jan 25, 2017</span>
      <span><svg width="12" height="11" viewBox="0 0 12 11"><path d="M1 1h10v7H5l-3 2V8H1z" fill="none" stroke="#888"/></svg>2 comments</span>
      <span><svg width="11" height="11" viewBox="0 0 11 11"><path d="M2 9 9 2" stroke="#888" stroke-width="2"/></svg>by Dale</span>
    </div>
    <p class="post-excerpt">Sed ut perspiciatis unde omnis iste natus error sit voluptatem<br>accusantium doloremque laudantium, totam rem aperiam, eaque<br>ipsa quae ab illo inventore veritatis et quasi architecto beatae<br>vitae dicta sunt explicabo. Nemo enim ipsam</p>
    <span class="read-more">READ MORE &gt;&gt;</span>
  </div>
</article>

<nav class="pagination abs">
  <span class="wide">Prev</span><span>1</span><span>2</span><span>3</span><span>4</span><span>5</span><span>6</span><span>...</span><span>22</span><span class="wide">Next</span>
</nav>

<!-- sidebar -->
<aside class="widget abs" style="top:916px;height:413px">
  <div class="widget-head">Community</div>
  <div class="member">
    <div class="avatar" style="background:#c9b8a8" role="img" aria-label="Member portrait"></div>
    <div><p class="member-name">Mara Tindle</p><p class="member-role">Sed ut perspiciatis</p>
      <div class="stars"><svg width="50" height="9" viewBox="0 0 50 9"><g fill="#f2b01e"><circle cx="4" cy="4.5" r="3.5"/><circle cx="14" cy="4.5" r="3.5"/><circle cx="24" cy="4.5" r="3.5"/></g><g fill="#ccc"><circle cx="34" cy="4.5" r="3.5"/><circle cx="44" cy="4.5" r="3.5"/></g></svg></div></div>
  </div>
  <div class="member">
    <div class="avatar" style="background:#b8a898" role="img" aria-label="Member portrait"></div>
    <div><p class="member-name">Mara Tindle</p><p class="member-role">Sed ut perspiciatis</p>
      <div class="stars"><svg width="50" height="9" viewBox="0 0 50 9"><g fill="#f2b01e"><circle cx="4" cy="4.5" r="3.5"/><circle cx="14" cy="4.5" r="3.5"/><circle cx="24" cy="4.5" r="3.5"/></g><g fill="#ccc"><circle cx="34" cy="4.5" r="3.5"/><circle cx="44" cy="4.5" r="3.5"/></g></svg></div></div>
  </div>
  <div class="member">
    <div class="avatar" style="background:#c8a898" role="img" aria-label="Member portrait"></div>
    <div><p class="member-name">Mara Tindle</p><p class="member-role">Sed ut perspiciatis</p>
      <div class="stars"><svg width="50" height="9" viewBox="0 0 50 9"><g fill="#f2b01e"><circle cx="4" cy="4.5" r="3.5"/><circle cx="14" cy="4.5" r="3.5"/><circle cx="24" cy="4.5" r="3.5"/></g><g fill="#ccc"><circle cx="34" cy="4.5" r="3.5"/><circle cx="44" cy="4.5" r="3.5"/></g></svg></div></div>
  </div>
</aside>

<aside class="widget abs" style="top:1358px;height:510px">
  <div class="widget-head">Recent Posts</div>
  <div class="recent">
    <div class="recent-thumb" style="background:linear-gradient(150deg,#7a5a6a,#c07a4a 50%,#3a4a5a)" role="img" aria-label="Graffiti covered laneway"></div>
    <div><p class="recent-title">Nemo enim ipsam</p>
      <div class="stars"><svg width="50" height="9" viewBox="0 0 50 9"><g fill="#f2b01e"><circle cx="4" cy="4.5" r="3.5"/><circle cx="14" cy="4.5" r="3.5"/><circle cx="24" cy="4.5" r="3.5"/></g><g fill="#ccc"><circle cx="34" cy="4.5" r="3.5"/><circle cx="44" cy="4.5" r="3.5"/></g></svg></div>
      <p class="recent-text">Lorem ipsum dolor sit<br>amet, consectetur</p>
      <p class="recent-meta"><svg width="11" height="10" viewBox="0 0 12 11"><path d="M1 1h10v7H5l-3 2V8H1z" fill="none" stroke="#888"/></svg>2 comments</p></div>
  </div>
  <div class="recent">
    <div class="recent-thumb" style="background:linear-gradient(180deg,#5a9ad8,#a8c8e0 50%,#8a5a3a)" role="img" aria-label="Person on a beach under a blue sky"></div>
    <div><p class="recent-title">Nemo enim ipsam</p>
      <div class="stars"><svg width="50" height="9" viewBox="0 0 50 9"><g fill="#f2b01e"><circle cx="4" cy="4.5" r="3.5"/><circle cx="14" cy="4.5" r="3.5"/><circle cx="24" cy="4.5" r="3.5"/></g><g fill="#ccc"><circle cx="34" cy="4.5" r="3.5"/><circle cx="44" cy="4.5" r="3.5"/></g></svg></div>
      <p class="recent-text">Lorem ipsum dolor sit<br>amet, consectetur</p>
      <p class="recent-meta"><svg width="11" height="10" viewBox="0 0 12 11"><path d="M1 1h10v7H5l-3 2V8H1z" fill="none" stroke="#888"/></svg>2 comments</p></div>
  </div>
  <div class="recent">
    <div class="recent-thumb" style="background:linear-gradient(180deg,#101828,#5a2a4a 55%,#1a2030)" role="img" aria-label="Fireworks over a city at night"></div>
    <div><p class="recent-title">Nemo enim ipsam</p>
      <div class="stars"><svg width="50" height="9" viewBox="0 0 50 9"><g fill="#f2b01e"><circle cx="4" cy="4.5" r="3.5"/><circle cx="14" cy="4.5" r="3.5"/><circle cx="24" cy="4.5" r="3.5"/></g><g fill="#ccc"><circle cx="34" cy="4.5" r="3.5"/><circle cx="44" cy="4.5" r="3.5"/></g></svg></div>
      <p class="recent-text">Lorem ipsum dolor sit<br>amet, consectetur</p>
      <p class="recent-meta"><svg width="11" height="10" viewBox="0 0 12 11"><path d="M1 1h10v7H5l-3 2V8H1z" fill="none" stroke="#888"/></svg>2 comments</p></div>
  </div>
</aside>

<aside class="widget abs" style="top:1924px;height:259px">
  <div class="widget-head">Archives</div>
  <ul class="archive-list">
    <li>June 2017</li><li>December 2010</li><li>November 2010</li><li>October 2010</li><li>September 2010</li><li>August 2010</li><li>May 2010</li>
  </ul>
</aside>

<div class="video-thumb abs" role="img" aria-label="Video still of a colonnaded public building with people on the lawn"></div>
<svg class="video-play abs" width="52" height="52" viewBox="0 0 52 52"><circle cx="26" cy="26" r="24" fill="none" stroke="#fff" stroke-width="2.5"/><path d="M21 16v20l16-10z" fill="#fff"/></svg>
<p class="video-text abs">Lorem ipsum dolor sit amet, consectetur<br>adipiscing elit, sed do eiusmod tempor incididunt</p>

<!-- footer -->
<footer class="site-footer abs"></footer>
<h3 class="foot-head abs" style="left:99px">Sign up to receive email</h3>
<p class="foot-text abs" style="left:99px;top:2697px">Excepteur sint occaecat cupidatat non proident, sunt in<br>culpa qui Nemo enim ipsam voluptatem</p>
<div class="email-field abs">Email</div>
<div class="subscribe-btn abs">SUBSCRIBE</div>

<h3 class="foot-head abs" style="left:460px">Contact us</h3>
<div class="abs" style="left:460px;top:2696px">
  <div class="contact-row"><svg width="12" height="16" viewBox="0 0 12 16"><path d="M6 1a5 5 0 0 1 5 5c0 4-5 9-5 9S1 10 1 6a5 5 0 0 1 5-5z" fill="#ddd"/><circle cx="6" cy="6" r="2" fill="#1c1c1c"/></svg><span>72 Wattle Lane, Suite 300<br>Brookvale NSW 2100</span></div>
  <div class="contact-row"><svg width="12" height="16" viewBox="0 0 12 16"><path d="M2 3c1-2 3-2 3 0l-1 2c1 2 2 4 4 5l2-1c2 0 2 2 0 3-5 1-9-6-8-9z" fill="#ddd"/></svg><span>Phone: (02) 5550 1487</span></div>
  <div class="contact-row"><svg width="12" height="16" viewBox="0 0 12 16"><rect x="0.5" y="4" width="11" height="8" fill="#ddd"/><path d="M.5 4 6 9l5.5-5" fill="none" stroke="#1c1c1c"/></svg><span>info@loosesaltbush.com</span></div>
</div>

<h3 class="foot-head abs" style="left:728px">Quick links</h3>
<ul class="quick-links abs" style="left:728px;top:2694px">
  <li>Home</li><li>Cultural</li><li>About Us</li><li>Videos</li><li>Subscriptions</li><li>Contacts</li>
</ul>

<h3 class="foot-head abs" style="left:928px">Social media</h3>
<div class="social fb abs" style="left:932px;top:2701px">68,876<br>Fans</div>
<div class="social tw abs" style="left:1023px;top:2701px">65<br>Followers</div>
<div class="social in abs" style="left:932px;top:2786px">68,876<br>Fans</div>
<div class="social yt abs" style="left:1023px;top:2786px">65<br>Followers</div>

<div class="foot-rule abs"></div>
<p class="copyright abs">Copyright © Loose Saltbush 2017. All rights reserved.</p>

</body>
</html>
```